QuillMark Business Cards

I need a business card designed for QuillMark. To get an idea of what we do please visit https://formvault.example/para-creadores-3

```html
<!DOCTYPE html>
<html lang="en">
<head>
<meta charset="utf-8">
<title>QuillMark Business Cards</title>
<link rel="stylesheet" href="https://fonts.googleapis.com/css2?family=Source+Sans+3:wght@400;600;700&display=swap">
<style>
  :root {
    --stage: #e4e4e4;
    --orange: #e0922a;
    --orange-deep: #d3861f;
    --orange-soft: #f1e6d8;
    --card-white: #f4f4f4;
    --ink: #2b2b2b;
    --white: #ffffff;
  }
  * { margin: 0; padding: 0; box-sizing: border-box; }
  html, body { width: 1200px; height: 960px; overflow: hidden; }
  body {
    background: var(--stage);
    font-family: "Source Sans 3", "Helvetica Neue", Arial, sans-serif;
    position: relative;
  }
  .card {
    position: absolute;
    left: 300px;
    width: 608px;
    height: 348px;
    overflow: hidden;
  }
  .card-front { top: 110px; }
  .card-back { top: 512px; background: var(--card-white); }

  .front-pattern {
    position: absolute; inset: 0;
    background: linear-gradient(100deg, #e39a3a 0%, var(--orange) 45%, var(--orange-deep) 100%);
  }
  .lockup { position: absolute; }
  .wordmark {
    font-weight: 400;
    line-height: 1;
    white-space: nowrap;
  }
  .tagline {
    display: flex; align-items: center; gap: 6px;
    letter-spacing: 0.22em; white-space: nowrap;
  }
  .tagline .rule { height: 1px; flex: 1; }

  .card-front .lockup { left: 220px; top: 150px; width: 274px; color: var(--white); }
  .card-front .wordmark { font-size: 34px; letter-spacing: 0.34em; }
  .card-front .tagline { font-size: 9px; margin-top: 10px; }
  .card-front .tagline .rule { background: var(--white); }

  .back-decoration {
    position: absolute; left: 330px; top: 0; width: 278px; height: 348px;
    background: radial-gradient(ellipse at 60% 50%, var(--orange-soft) 0%, rgba(241,230,216,0) 75%);
  }
  .card-back .lockup { left: 123px; top: 58px; width: 206px; color: var(--ink); }
  .card-back .wordmark { font-size: 25px; letter-spacing: 0.37em; }
  .card-back .tagline { color: var(--orange); font-size: 8px; margin-top: 8px; }
  .card-back .tagline .rule { background: var(--ink); }

  .person { position: absolute; right: 35px; top: 156px; text-align: right; }
  .person-name { color: var(--orange); font-weight: 700; font-size: 19px; line-height: 1.1; }
  .person-role { color: var(--ink); font-size: 15px; margin-top: 3px; }

  .address {
    position: absolute; left: 42px; top: 208px;
    font-size: 15px; line-height: 20px; color: var(--ink); font-style: normal;
  }
  .contacts {
    position: absolute; left: 42px; top: 257px; list-style: none;
    font-size: 15px; line-height: 20.5px; color: var(--ink);
  }
  .contacts li { display: flex; align-items: center; gap: 6px; }
  .contacts svg { width: 13px; height: 13px; flex: none; }
</style>
</head>
<body>
  <section class="card card-front" aria-label="Card front">
    <div class="front-pattern" role="img" aria-label="Orange background with a repeating geometric line pattern"></div>
    <div class="lockup">
      <div class="wordmark">QUILLMARK</div>
      <div class="tagline"><span>DIGITAL NOTARY</span><span class="rule"></span></div>
    </div>
  </section>

  <section class="card card-back" aria-label="Card back">
    <div class="back-decoration" role="img" aria-label="Faint large brand symbol decoration"></div>
    <div class="lockup">
      <div class="wordmark">QUILLMARK</div>
      <div class="tagline"><span>DIGITAL NOTARY</span><span class="rule"></span></div>
    </div>
    <div class="person">
      <div class="person-name">Daniel Reyes</div>
      <div class="person-role">Owner</div>
    </div>
    <address class="address">48 Harbor Lane<br>Coral Point, Florida, 33100</address>
    <ul class="contacts">
      <li>
        <svg viewBox="0 0 16 16" fill="none" stroke="#e0922a" stroke-width="1.6" stroke-linecap="round" stroke-linejoin="round"><path d="M3 2h3l1.5 3.5-2 1.2a8 8 0 0 0 3.8 3.8l1.2-2L14 10v3a1 1 0 0 1-1 1A11 11 0 0 1 2 3a1 1 0 0 1 1-1z"/></svg>
        (305) 555-0147
      </li>
      <li>
        <svg viewBox="0 0 16 16" fill="none" stroke="#e0922a" stroke-width="1.6" stroke-linejoin="round"><rect x="1.5" y="3.5" width="13" height="9"/><path d="M1.5 3.5 8 9l6.5-5.5"/></svg>
        daniel@quillmark.example
      </li>
      <li>
        <svg viewBox="0 0 16 16" fill="none" stroke="#e0922a" stroke-width="1.4"><circle cx="8" cy="8" r="6.3"/><ellipse cx="8" cy="8" rx="2.8" ry="6.3"/><path d="M1.7 8h12.6M2.8 4.8h10.4M2.8 11.2h10.4"/></svg>
        www.quillmark.example
      </li>
    </ul>
  </section>
</body>
</html>
```